Postcard Design

R.K Landscaping 484-883-7758Mulching Mowing Planting Spring and Fall Clean up

The colors I would like to work with Are black and green.I do have a Facebook page it's https://www.example-social.test/RK-Landscaping-904417362018834/

For my business logo I would like to put that either on the corner or in the background

Services: mowing, mulching, fall and spring cleanup, hedge trimming

Industry/Entity Type

Landscaping

Requirements
Must have
• Please use these pics
• I like Design #9926064
• and room for addresses to
Should not have
• the pics in the back of card

```html
<!DOCTYPE html>
<html lang="en">
<head>
<meta charset="utf-8">
<title>R.K Landscaping Postcard</title>
<link rel="stylesheet" href="https://fonts.googleapis.com/css2?family=Oswald:wght@400&family=Mukta:wght@400;500&display=swap">
<style>
  :root{
    --stage:#2a2a2a;
    --ink:#231f20;
    --green:#4cb848;
    --green-light:#6cc04a;
    --white:#ffffff;
    --text:#333333;
    --panel-top:#ffffff;
    --panel-bottom:#dcdcdc;
  }
  *{margin:0;padding:0;box-sizing:border-box}
  html,body{width:900px;height:1200px;overflow:hidden;background:var(--stage)}
  .canvas{position:relative;width:900px;height:1200px}

  .card{position:absolute;left:98px;width:705px;height:545px;overflow:hidden}
  .card--front{top:33px;background:var(--ink)}
  .card--back{top:623px;background:var(--white)}

  .hero-photo{position:absolute;inset:0;
    background:linear-gradient(180deg,#8fbde6 0%,#c9def0 22%,#5f8f3f 45%,#4d7a2e 70%,#3c6424 100%)}
  .front-shapes{position:absolute;inset:0}

  .brand{position:absolute;left:20px;top:180px;width:230px;text-align:center;
    font-family:"Mukta",sans-serif;font-weight:500;font-size:30px;line-height:1;color:var(--white)}

  .services{position:absolute;left:0;top:305px;width:260px}
  .services__title{background:var(--green);height:40px;padding-left:32px;
    font-family:"Mukta",sans-serif;font-weight:400;font-size:29px;line-height:42px;color:var(--white)}
  .services__list{list-style:none;margin-top:17px}
  .services__item{display:flex;align-items:center;gap:10px;background:var(--green-light);
    height:31px;margin-bottom:11px;padding-left:34px;
    font-family:"Oswald",sans-serif;font-weight:400;font-size:20px;color:var(--white)}
  .services__item svg{width:18px;height:18px;flex:none}

  .snapshot{position:absolute;border-radius:50%;border:5px solid var(--white)}
  .snapshot--sign{left:327px;top:349px;width:118px;height:118px;
    background:radial-gradient(circle at 50% 40%,#f0f0f0 0%,#7ea25a 45%,#4e7431 100%)}
  .snapshot--walk{left:494px;top:327px;width:140px;height:140px;
    background:linear-gradient(180deg,#8aa2c2 0%,#a9b6c6 40%,#5d8a3a 60%,#c9a486 80%,#6b8c44 100%)}

  .call{position:absolute;left:290px;top:492px;display:flex;align-items:center;gap:12px;
    font-family:"Mukta",sans-serif;font-weight:400;font-size:28px;color:var(--white)}
  .call svg{width:26px;height:26px}

  .back-shapes{position:absolute;left:0;top:0}
  .about{position:absolute;left:20px;top:44px;width:240px;display:flex;gap:12px}
  .about svg{width:18px;height:18px;flex:none;margin-top:3px}
  .about p{width:205px;font-family:"Mukta",sans-serif;font-weight:400;font-size:17px;line-height:21px;color:var(--text)}

  .contact{position:absolute;left:0;top:307px;width:327px;height:117px;background:var(--green);
    font-family:"Mukta",sans-serif;font-weight:400;color:var(--text)}
  .contact__title{position:absolute;left:25px;top:8px;font-size:21px;color:var(--white)}
  .contact__row{position:absolute;display:flex;align-items:center;gap:6px;font-size:15.5px}
  .contact__row svg{width:14px;height:16px}
  .contact__row--addr1{left:24px;top:42px}
  .contact__row--addr2{left:47px;top:68px}
  .contact__row--mail{left:24px;top:91px}
  .contact__row--follow{left:174px;top:14px;color:var(--white);font-size:16px}
  .contact__row--phone{left:174px;top:42px;color:var(--white)}
  .dot{display:inline-block;width:18px;height:18px;border-radius:50%;background:var(--white);margin-left:6px}

  .mail-brand{position:absolute;left:470px;top:92px;width:120px;text-align:center;
    font-family:"Mukta",sans-serif;font-weight:500;font-size:14px;line-height:1;color:var(--ink)}
  .stamp-box{position:absolute;left:592px;top:32px;width:84px;height:98px;border:1px solid var(--ink)}
</style>
</head>
<body>
<div class="canvas">

  <section class="card card--front">
    <div class="hero-photo" role="img" aria-label="Photo of a landscaped backyard with mowed lawn, trees, wooden deck and two-storey house"></div>
    <svg class="front-shapes" viewBox="0 0 705 545" width="705" height="545" aria-hidden="true">
      <path d="M0,200 C60,330 200,420 330,428 C480,436 620,390 705,352 L705,545 L0,545 Z" fill="var(--white)"/>
      <path d="M0,212 C60,338 200,432 330,440 C480,448 620,400 705,366 L705,545 L0,545 Z" fill="var(--green)"/>
      <path d="M0,232 C60,350 200,446 330,455 C480,462 620,414 705,382 L705,545 L0,545 Z" fill="var(--ink)"/>
    </svg>

    <div class="brand">R.K Landscaping</div>

    <div class="services">
      <h2 class="services__title">Our Services</h2>
      <ul class="services__list">
        <li class="services__item"><svg viewBox="0 0 20 20"><circle cx="10" cy="10" r="8" fill="none" stroke="#fff" stroke-width="2"/><path d="M6 10l3 3 5-6" fill="none" stroke="#fff" stroke-width="2"/></svg>Mulching Mowing</li>
        <li class="services__item"><svg viewBox="0 0 20 20"><circle cx="10" cy="10" r="8" fill="none" stroke="#fff" stroke-width="2"/><path d="M6 10l3 3 5-6" fill="none" stroke="#fff" stroke-width="2"/></svg>Planting Plants</li>
        <li class="services__item"><svg viewBox="0 0 20 20"><circle cx="10" cy="10" r="8" fill="none" stroke="#fff" stroke-width="2"/><path d="M6 10l3 3 5-6" fill="none" stroke="#fff" stroke-width="2"/></svg>Fall &amp; Spring Clean up</li>
        <li class="services__item"><svg viewBox="0 0 20 20"><circle cx="10" cy="10" r="8" fill="none" stroke="#fff" stroke-width="2"/><path d="M6 10l3 3 5-6" fill="none" stroke="#fff" stroke-width="2"/></svg>Hedge Trimming</li>
      </ul>
    </div>

    <div class="snapshot snapshot--sign" role="img" aria-label="Photo of a business sign with flower bed planting"></div>
    <div class="snapshot snapshot--walk" role="img" aria-label="Photo of a new stone walkway and mulched bed beside a house"></div>

    <div class="call">Call Now:
      <svg viewBox="0 0 26 26"><circle cx="13" cy="13" r="11" fill="none" stroke="var(--green)" stroke-width="2.5"/><path d="M9 8c0 5 4 9 9 9l1-2-2.5-1.5-1.5 1c-1.5-.7-2.8-2-3.5-3.5l1-1.5L11 7z" fill="var(--green)"/></svg>
      555-216-0493</div>
  </section>

  <section class="card card--back">
    <svg class="back-shapes" viewBox="0 0 705 545" width="705" height="545" aria-hidden="true">
      <defs>
        <linearGradient id="panelFade" x1="0" y1="0" x2="0" y2="1">
          <stop offset="0" stop-color="var(--panel-top)"/>
          <stop offset="1" stop-color="var(--panel-bottom)"/>
        </linearGradient>
      </defs>
      <path d="M0,0 L250,0 C300,90 312,220 302,307 L0,307 Z" fill="url(#panelFade)"/>
      <path d="M270,0 L300,0 C345,110 337,240 329,307 L316,307 C324,220 320,90 270,0 Z" fill="var(--ink)"/>
      <path d="M245,0 L278,0 C326,95 324,220 314,307 L300,307 C311,220 300,90 245,0 Z" fill="var(--green)"/>
    </svg>

    <div class="about">
      <svg viewBox="0 0 20 20"><circle cx="10" cy="10" r="8" fill="none" stroke="var(--green)" stroke-width="2"/><path d="M6 10l3 3 5-6" fill="none" stroke="var(--green)" stroke-width="2"/></svg>
      <p>Lorem Ipsum is simply dummy text of the printing and typesetting industry. Lorem Ipsum has been the industry's standard dummy text ever since the 1500s, when an unknown printer took a galley of type and scrambled it to make a type specimen book.</p>
    </div>

    <div class="contact">
      <div class="contact__title">Contact info</div>
      <div class="contact__row contact__row--follow">Follow Us<span class="dot"></span><span class="dot"></span></div>
      <div class="contact__row contact__row--addr1"><svg viewBox="0 0 14 16"><circle cx="7" cy="5" r="3.5" fill="none" stroke="#fff" stroke-width="1.8"/><path d="M7 9v5M3 15h8" stroke="#fff" stroke-width="1.8"/></svg>Address line 1</div>
      <div class="contact__row contact__row--addr2">Address line 2</div>
      <div class="contact__row contact__row--mail"><svg viewBox="0 0 14 16"><rect x="1" y="4" width="12" height="9" fill="none" stroke="#fff" stroke-width="1.3"/><path d="M1 4l6 5 6-5" fill="none" stroke="#fff" stroke-width="1.3"/></svg>yourmail@example.com</div>
      <div class="contact__row contact__row--phone"><svg viewBox="0 0 16 16"><circle cx="8" cy="8" r="6.5" fill="none" stroke="#fff" stroke-width="1.4"/><path d="M5.5 5c0 3 2.5 5.5 5.5 5.5l.6-1.2-1.5-.9-.9.6c-.9-.4-1.7-1.2-2.1-2.1l.6-.9L7 5.2z" fill="#fff"/></svg>555-216-0493</div>
    </div>

    <div class="mail-brand">R.K Landscaping</div>
    <div class="stamp-box"></div>
  </section>

</div>
</body>
</html>
```